El Molinete Postcard

Please refer to our site for inspiration - I know this is alot of info but ?

El Molinete Reception Hall
4187C Quillmont Rd, Benicia, CA 707-555-0142
www.El-Molinete.example

Located in Benicia, California, we are a new venue that can host a variety of events. We can provide an exceptional space for your next party, reception, quinceañera, birthday party, or meeting! We treat each client with respect and go out of our way to accommodate all of your needs and make your event a success. Conveniently located just off the 680/780 junction, El Molinete is located in a safe, well-lit area with a large private parking area.

The space comes prepared with everything you need to get your party started – chairs and tables with tablecloths, a well-equipped kitchen, and incredible decorations to set the perfect backdrop to your event! Rent just the Lounge for a more intimate get-together, or add the Main Hall for your large sit-down event.

Lounge – Beautiful 1,600 ft2 entry room featuring large living room with conversation sofa seating for 40+ Sound system  Pass-through bar with seating  Fully-equipped 200 ft2 kitchen with
4-burner gas stove, oven, large double sink, full-size refrigerator, 2 microwaves, and ice machine, plus lots of storage and counter space  Newly-remodeled Men’s and Women’s bathrooms

Main Hall – Spacious 24’x80’ room with seating for up to 160 people  2,000 ft2  72” round tables with chairs, each seating up to 8 guests  DJ stand and Sound system  Atmospheric lighting
_______________________________________
Pricing -
Daytime Parties
Available 8AM-2PM
4-hour minimum

Lounge and Kitchen Only
Fri - Sat - Sun : $80/hr
Mon - Thurs : $60/hr

All Areas: Lounge, Kitchen, Main Hall, and Backyard
Fri - Sat - Sun : $120/hr
Mon - Thurs : $100/hr
___________________________________________
Evening Events
Available 3PM-12AM
5-hour minimum

Lounge and Kitchen Only -
Fri - Sat - Sun : $100/hr
Mon - Thurs : $50/hr

Fri - Sat - Sun : $160/hr
Mon - Thurs : $75/hr
___________________________________________________
Looking for a different time frame, all-day rental, or other special request? Let us know!
We'd be happy to provide you with a custom quote for your event.

I am not going to mail this postcard - only a hand out I need info and pricing on back

This is a hand out - will not be mailed

Only need my text on back

• Text and pricing on back
• Vintage feel to it

```html
<!DOCTYPE html>
<html lang="en">
<head>
<meta charset="utf-8">
<title>El Molinete Postcard</title>
<link href="https://fonts.googleapis.com/css2?family=Didact+Gothic&family=Arimo&display=swap" rel="stylesheet">
<style>
  :root {
    --stage: #ece8e2;
    --slate: #2b3136;
    --ink: #111;
    --paper: #ffffff;
    --soft-white: #e9ecec;
    --muted-teal: #8fb2a9;
    --teal: #4d918b;
    --teal-light: #7fc0ba;
    --blue: #3f87b9;
    --blue-mid: #4f82a9;
    --blue-deep: #38658c;
    --green: #5d9c86;
    --rust: #b2603a;
  }
  * { margin: 0; padding: 0; box-sizing: border-box; }
  html, body { width: 1200px; height: 1000px; overflow: hidden; }
  body {
    position: relative;
    background: var(--stage);
    font-family: "Didact Gothic", "Century Gothic", sans-serif;
  }

  /* ---------- Back of card ---------- */
  .card-back {
    position: absolute; left: 20px; top: 32px;
    width: 655px; height: 545px;
    background: var(--slate);
    color: var(--soft-white);
    overflow: hidden;
  }
  .stripe { position: absolute; height: 16px; }
  .stripe--a { left: 0; top: 0; width: 488px; background: var(--blue); }
  .stripe--b { left: 488px; top: 0; width: 67px; background: var(--green); }
  .stripe--c { left: 555px; top: 0; width: 100px; background: var(--rust); height: 16px; }
  .stripe--d { left: 0; top: 16px; width: 555px; background: var(--blue-mid); }
  .stripe--e { left: 0; top: 32px; width: 488px; background: var(--blue-deep); height: 14px; }

  .features {
    position: absolute; left: 27px; top: 58px; width: 300px;
    font-size: 12px; line-height: 14.6px;
  }
  .features__heading { color: var(--muted-teal); }
  .features__list { list-style: none; margin-bottom: 16px; }
  .features__list li { padding-left: 10px; position: relative; }
  .features__list li::before { content: "•"; position: absolute; left: 0; }

  .intro {
    position: absolute; left: 345px; top: 58px; width: 290px;
    font-size: 12px; line-height: 14.6px; font-style: italic;
  }
  .intro__lead { color: var(--muted-teal); font-size: 15px; }

  .pricing {
    position: absolute; left: 333px; top: 165px; width: 300px; height: 193px;
    background: var(--teal);
    font-size: 10.5px; line-height: 12.4px; text-align: center;
  }
  .pricing__title { font-size: 13px; margin-top: 10px; margin-bottom: 10px; }
  .pricing__cols { display: flex; }
  .pricing__col { flex: 1; }
  .pricing__col p { margin-bottom: 12px; }

  .photo { position: absolute; }
  .photo--lounge {
    left: 0; top: 365px; width: 328px; height: 180px;
    background: linear-gradient(180deg, #6d5b48 0%, #8a7357 45%, #3e3126 100%);
  }
  .photo--bar {
    left: 333px; top: 365px; width: 322px; height: 180px;
    background: linear-gradient(180deg, #4a3d31 0%, #8b7a63 50%, #5a4a3a 100%);
  }

  /* ---------- Front of card ---------- */
  .card-front {
    position: absolute; left: 527px; top: 440px;
    width: 653px; height: 545px;
    background: var(--paper);
    overflow: hidden;
  }
  .photo--hall {
    left: 0; top: 0; width: 300px; height: 545px;
    background: linear-gradient(180deg, #3c3c3c 0%, #6a6a6a 18%, #6fa9a3 28%, #7fc0ba 60%, #8fcac4 100%);
  }
  .edge-band { position: absolute; left: 300px; top: 0; width: 12px; height: 545px; background: #0c0c0c; }

  .wordmark {
    position: absolute; left: 18px; top: 60px;
    font-size: 46px; color: var(--paper); line-height: 1;
  }
  .front-copy {
    position: absolute; left: 20px; top: 122px; width: 275px;
    font-size: 13.5px; line-height: 16.6px; color: var(--ink);
  }
  .front-callout {
    position: absolute; left: 18px; top: 320px; width: 282px;
    font-size: 14px; line-height: 17px; font-style: italic; text-align: center; color: var(--ink);
  }
  .front-callout p + p { margin-top: 17px; }

  .postage {
    position: absolute; left: 488px; top: 17px; width: 145px; height: 156px;
    border: 2px solid var(--ink);
    font-family: "Arimo", Arial, sans-serif; font-size: 22px; line-height: 29px;
    text-align: center; padding-top: 46px;
  }
  .return-address {
    position: absolute; left: 316px; top: 460px;
    font-family: "Arimo", Arial, sans-serif; font-size: 14.5px; line-height: 19px; color: var(--ink);
  }
</style>
</head>
<body>

<section class="card-back">
  <div class="stripe stripe--a"></div>
  <div class="stripe stripe--b"></div>
  <div class="stripe stripe--c"></div>
  <div class="stripe stripe--d"></div>
  <div class="stripe stripe--e"></div>

  <div class="features">
    <p class="features__heading">Lounge – Beautiful 1,600 ft2 entry room featuring large living room with conversation sofa seating for 40+ Sound system</p>
    <ul class="features__list">
      <li>Pass-through bar with seating</li>
      <li>Fully-equipped 200 ft2 kitchen with<br>4-burner gas stove, oven, large double<br>sink, full-size refrigerator, 2 microwaves,<br>and ice machine, plus lots of storage<br>and counter space</li>
      <li>Newly-remodeled Men’s and Women’s<br>bathrooms</li>
    </ul>
    <p class="features__heading">Main Hall – Spacious 24’x80’ room with seating for up to 160 people</p>
    <ul class="features__list">
      <li>2,000 ft2</li>
      <li>72” round tables with chairs, each<br>seating up to 8 guests</li>
      <li>DJ stand and Sound system</li>
      <li>Atmospheric lighting</li>
    </ul>
  </div>

  <p class="intro"><span class="intro__lead">The space</span> comes prepared with everything you need to get your party started – chairs and tables with tablecloths, a well-equipped kitchen, and incredible decorations to set the perfect backdrop to your event! Rent just the Lounge for a more intimate get-together, or add the Main Hall for your large sit-down event.</p>

  <div class="pricing">
    <h2 class="pricing__title">Pricing</h2>
    <div class="pricing__cols">
      <div class="pricing__col">
        <p>Daytime Parties<br>Available 8AM-2PM<br>4-hour minimum</p>
        <p>Lounge and Kitchen Only<br>Fri - Sat - Sun : $80/hr<br>Mon - Thurs : $60/hr</p>
        <p>All Areas: Lounge, Kitchen,<br>Main Hall, and Backyard<br>Fri - Sat - Sun : $120/hr<br>Mon - Thurs : $100/hr</p>
      </div>
      <div class="pricing__col">
        <p>Evening Events<br>Available 3PM-12AM<br>5-hour minimum</p>
        <p>Lounge and Kitchen Only<br>Fri - Sat - Sun : $100/hr<br>Mon - Thurs : $50/hr</p>
        <p>All Areas: Lounge, Kitchen,<br>Main Hall, and Backyard<br>Fri - Sat - Sun : $160/hr<br>Mon - Thurs : $75/hr</p>
      </div>
    </div>
  </div>

  <div class="photo photo--lounge" role="img" aria-label="Photo of the lounge with sofas, armchairs and globe pendant lights"></div>
  <div class="photo photo--bar" role="img" aria-label="Photo of the pass-through bar with a food spread and globe lights"></div>
</section>

<section class="card-front">
  <div class="photo photo--hall" role="img" aria-label="Photo of the main hall with string lights, round tables and chairs"></div>
  <div class="edge-band"></div>

  <h1 class="wordmark">El Molinete</h1>

  <p class="front-copy">Located in Benicia, California, we are a new venue that can host a variety of events. We can provide an exceptional space for your next party, reception, quinceañera, birthday party, or meeting! We treat each client with respect and go out of our way to accommodate all of your needs and make your event a suc-cess. Conveniently located just off the 680/780 junction, El Molinete is located in a safe, well-lit area with a large private</p>

  <div class="front-callout">
    <p>Looking for a different time frame,<br>all-day rental, or other special request?</p>
    <p>Let us know!<br>We’d be happy to provide you with a<br>custom quote for your event.</p>
  </div>

  <div class="postage">Postage<br>Area</div>

  <address class="return-address" style="font-style:normal">
    El Molinete Reception Hall<br>
    4187C Quillmont Rd, Benicia, CA 707-555-0142<br>
    www.El-Molinete.example
  </address>
</section>

</body>
</html>
```